Italian Dinning Table and wardrobe Selling Website

We need a website design for a reputable furniture company deals in the manufacture of Italian dinning tables and wardrobe. We provide our services to USA based customers.

The categories of the website are
- Home page
- Product page
- The page where all the items are sold
- The shopping cart page

The website is required to have several areas of products with prices that can be added to shopping cart.
Also the website should have customer login facility along with privacy policy, contact us, about us and terms of use
Preferred colors are brown, black and pink,

It Company

```html
<!DOCTYPE html>
<html lang="en">
<head>
<meta charset="utf-8">
<title>Casa Tavola — Italian Dining &amp; Wardrobes</title>
<link href="https://fonts.googleapis.com/css2?family=Open+Sans:ital,wght@0,300;0,400;0,600;0,700;1,400&family=Roboto+Condensed:wght@400;700&family=Dancing+Script:wght@600&display=swap" rel="stylesheet">
<style>
:root{
  --brown:#7a3d0b;
  --brown-dark:#5e2d05;
  --ink:#222;
  --pink:#f6a6c8;
  --pink-soft:#fbd3e4;
  --price:#b42a35;
  --grey-bg:#ececec;
  --card:#fafafa;
  --muted:#999;
  --bar:#1e1e1e;
  --star:#f2a223;
}
*{box-sizing:border-box;margin:0;padding:0}
html,body{width:673px;height:1200px;overflow:hidden}
body{position:relative;font-family:"Open Sans",Arial,sans-serif;color:var(--ink);background:#fff;font-size:7px}
.abs{position:absolute}
/* top bar */
.topbar{left:0;top:0;width:673px;height:18px;background:var(--brown);color:#fff}
.topbar .mail{left:79px;top:4px;font-size:7px;display:flex;align-items:center;gap:6px}
.topbar .account{left:486px;top:5px;font-size:6.5px}
.topbar .cart{left:525px;top:0;width:68px;height:18px;background:var(--bar);font-size:6.5px;display:flex;align-items:center;justify-content:center;gap:4px}
/* header */
.header{left:0;top:18px;width:673px;height:31px;border-bottom:1.5px solid var(--pink-soft);background:#fff}
.brand{left:79px;top:10px;display:flex;align-items:center;gap:5px;font-weight:700;font-size:9.5px;letter-spacing:.5px;color:var(--ink)}
.brand .mark{width:9px;height:9px;background:var(--brown)}
.nav{left:270px;top:12px;display:flex;gap:14px;font-size:6.8px;font-weight:600;color:#333}
.nav .active{border-bottom:1.5px solid var(--pink);padding-bottom:3px}
.tools{left:524px;top:10px;display:flex;gap:6px;align-items:center}
.tools .search{width:13px;height:12px;background:var(--pink);display:flex;align-items:center;justify-content:center}
.tools .dot{width:7px;height:7px;border-radius:50%;background:#b5b5b5}
/* hero */
.hero{left:0;top:49px;width:673px;height:245px;background:linear-gradient(100deg,#7e6a66 0%,#a58f86 35%,#c9b3a7 60%,#8d7672 100%)}
.hero .kicker{left:79px;top:77px;color:#fff;font-weight:300;font-size:16px;letter-spacing:.3px}
.hero h1{left:79px;top:91px;color:#fff;font-weight:700;font-size:26px;letter-spacing:.5px}
.hero .btn{left:79px;top:124px;width:59px;height:21px;border:1.5px solid #fff;color:#fff;font-size:7px;font-weight:600;display:flex;align-items:center;justify-content:center}
.dots{display:flex;gap:2px}
.dots span{width:3.5px;height:3.5px;border-radius:50%;border:0.8px solid #fff}
.dots span.on{background:#fff}
/* deals */
.deals{left:80px;top:296px;width:206px;height:182px;background:var(--pink);border:5px solid var(--pink-soft)}
.deals .title{left:0;width:196px;top:20px;text-align:center;font-family:"Dancing Script",cursive;font-size:20px;color:#4a2c22}
.deals .photo{left:27px;top:55px;width:98px;height:98px;border-radius:50%;background:#fff;padding:7px}
.deals .photo div{width:100%;height:100%;border-radius:50%;background:linear-gradient(#e9e2de,#c9bdb6)}
.deals .badge{left:117px;top:70px;width:64px;height:64px;border-radius:50%;background:var(--brown);border:3px solid #c06b2f;color:#fff;text-align:center;font-family:"Roboto Condensed",sans-serif}
.popular{left:289px;top:296px;width:304px;height:182px;border:1.5px solid var(--pink-soft);background:#fff}
.popular h2{left:36px;top:23px;font-size:12.5px;font-weight:400;letter-spacing:.3px}
.popular h2 b{font-weight:700}
.arrows{left:241px;top:25px;display:flex}
.arrows span{width:16px;height:16px;border:1px solid var(--pink);display:flex;align-items:center;justify-content:center}
.newtag{left:37px;top:55px;background:var(--pink);color:#fff;font-size:4.5px;font-weight:700;padding:1px 3px}
.popular .photo{left:37px;top:63px;width:150px;height:105px;background:linear-gradient(#f4f2f1,#d8d2ce)}
.popular .info{left:228px;top:75px;width:76px;text-align:left}
.pname{font-family:"Roboto Condensed",sans-serif;font-weight:700;font-size:7.5px;color:#222}
.stars{color:var(--star);font-size:6px;letter-spacing:.5px}
.popular .cat{font-size:5.5px;color:#555;margin-top:4px}
.popular .price{color:var(--price);font-weight:700;font-size:8px;margin-top:7px;text-align:right;padding-right:4px}
.popular .add{left:219px;top:136px;width:56px;height:17px;background:var(--pink);color:#fff;font-size:6.5px;display:flex;align-items:center;justify-content:center}
/* products */
.products{left:0;top:480px;width:673px;height:230px;background:var(--grey-bg)}
.tabs{left:0;width:673px;top:16px;display:flex;justify-content:center;gap:12px;font-size:10.5px;color:#aaa;align-items:center}
.tabs .on{color:#333;border-bottom:1.5px solid var(--pink);padding-bottom:2px;margin-top:2px}
.tabs i{font-style:normal;font-size:6px}
.card{top:52px;width:119px;height:143px;background:var(--card)}
.card .photo{left:24px;top:17px;width:71px;height:62px}
.card .pname{left:0;width:119px;top:90px;text-align:center}
.card .stars{left:0;width:119px;top:101px;text-align:center;font-size:5.5px}
.card .price{left:12px;top:119px;color:var(--price);font-weight:700;font-size:7.5px}
.card .heart{left:42px;top:119px}
.card .add{left:63px;top:114px;width:46px;height:17px;border:1px solid var(--pink);color:var(--pink);font-size:6.5px;display:flex;align-items:center;justify-content:center;background:#fff}
.card .add.on{background:var(--pink);color:#fff}
.wood{background:linear-gradient(#6d4a3c,#3d2a22)}
.light{background:linear-gradient(#f1efee,#cfc8c4)}
/* testimonials */
.testi{left:0;top:711px;width:673px;height:214px;background:linear-gradient(160deg,#3f3733 0%,#5a4b42 45%,#2d2624 100%)}
.testi h2{left:0;width:673px;top:39px;text-align:center;color:#fff;font-size:12.5px;font-weight:400}
.testi h2 b{font-weight:700}
.quote{left:142px;top:72px;width:389px;height:71px;background:rgba(122,61,11,.85)}
.quote .avatar{left:16px;top:11px;width:49px;height:49px;border-radius:50%;background:linear-gradient(#e8d6c7,#b98f73);border:2px solid #fff}
.quote .mark{left:74px;top:12px;color:#fff;font-size:18px;font-weight:700;line-height:1}
.quote p{left:94px;top:13px;width:282px;color:#fff;font-size:5.8px;font-style:italic;line-height:1.65}
.quote .who{left:94px;top:43px;color:#fff;font-size:6px}
/* newsletter */
.news-ico{left:79px;top:956px}
.news h3{font-size:10.5px;font-weight:400;line-height:1.05;color:#333}
.field{left:79px;top:989px;width:183px;height:21px;border:1px solid var(--pink-soft);display:flex;align-items:center;gap:5px;padding-left:7px;font-size:5.5px;color:#999}
.submit{left:262px;top:989px;width:51px;height:21px;background:var(--pink);color:#fff;font-size:7px;display:flex;align-items:center;justify-content:center}
.vline{left:330px;top:953px;width:1px;height:70px;background:#ddd}
.why{left:347px;top:955px;font-size:10.5px;color:#444}
.feat{top:975px;text-align:center;font-family:"Roboto Condensed",sans-serif;font-weight:700;font-size:5.8px;color:#333}
.feat svg{display:block;margin:0 auto 4px}
/* footer */
.footer{left:0;top:1043px;width:673px;height:128px;background:var(--brown);color:#fff}
.fcol{top:29px}
.fcol h4{font-family:"Roboto Condensed",sans-serif;font-size:6.5px;font-weight:700;letter-spacing:.3px;padding-bottom:6px;border-bottom:1px solid #9b5d2a;width:91px;margin-bottom:8px}
.fcol li{list-style:none;font-size:6.2px;line-height:12.8px}
.frow{display:flex;align-items:center;gap:6px}
.fdots{display:flex;gap:4px;margin-top:4px}
.fdots span{width:7px;height:7px;border-radius:50%;background:#fff}
.bottom{left:0;top:1171px;width:673px;height:29px;background:var(--bar);color:#ddd;font-size:5.5px}
</style>
</head>
<body>

<div class="abs topbar">
  <div class="abs mail"><svg width="7" height="5" viewBox="0 0 7 5"><rect width="7" height="5" fill="#fff"/><path d="M0 0l3.5 2.8L7 0" stroke="#7a3d0b" stroke-width=".8" fill="none"/></svg>hello@casatavola.com</div>
  <div class="abs account">Account ⌄</div>
  <div class="abs cart">My Cart
    <svg width="9" height="8" viewBox="0 0 9 8"><path d="M0 1h1.6l1.2 4.2h4.6L8.5 2H2.2" fill="none" stroke="#fff" stroke-width=".8"/><circle cx="3.4" cy="7" r=".7" fill="#fff"/><circle cx="6.8" cy="7" r=".7" fill="#fff"/></svg> 0</div>
</div>

<header class="abs header">
  <div class="abs brand"><span class="mark"></span>CASA TAVOLA</div>
  <nav class="abs nav"><span class="active">HOME</span><span>PRODUCTS</span><span>CONTACT US</span></nav>
  <div class="abs tools">
    <span class="search"><svg width="7" height="7" viewBox="0 0 7 7"><circle cx="3" cy="3" r="2.2" fill="none" stroke="#fff" stroke-width="1"/><path d="M4.6 4.6L6.6 6.6" stroke="#fff" stroke-width="1"/></svg></span>
    <span class="dot"></span><span class="dot"></span><span class="dot"></span><span class="dot"></span>
  </div>
</header>

<section class="abs hero" role="img" aria-label="Photo of an Italian dining room with a table, purple upholstered chairs and lamps">
  <div class="abs kicker">ITALIAN DINING</div>
  <h1 class="abs">COLLECTIONS</h1>
  <div class="abs btn">Shop Now !</div>
  <div class="abs dots" style="left:329px;top:235px"><span class="on"></span><span></span><span></span><span></span></div>
</section>

<section class="abs deals">
  <div class="abs title">Deals of the day</div>
  <div class="abs photo"><div role="img" aria-label="Photo of an open wardrobe with clothes"></div></div>
  <div class="abs badge">
    <div style="font-size:7px;margin-top:11px">UPTO</div>
    <div style="font-size:22px;font-weight:700;line-height:1">20<span style="font-size:11px;vertical-align:top">%</span></div>
    <div style="font-size:8px">OFF</div>
  </div>
</section>

<section class="abs popular">
  <h2 class="abs"><b>POPULAR</b> PRODUCTS</h2>
  <div class="abs arrows">
    <span><svg width="5" height="7" viewBox="0 0 5 7"><path d="M4 .5L1 3.5 4 6.5" stroke="#f6a6c8" fill="none"/></svg></span>
    <span><svg width="5" height="7" viewBox="0 0 5 7"><path d="M1 .5L4 3.5 1 6.5" stroke="#f6a6c8" fill="none"/></svg></span>
  </div>
  <div class="abs photo" role="img" aria-label="Photo of a dark wood dining table with four black chairs"></div>
  <div class="abs newtag">NEW</div>
  <div class="abs info">
    <div class="pname">TABLE NAME</div>
    <div class="stars" style="padding-left:18px">★★★★★</div>
    <div class="cat">Category No : 19860</div>
    <div class="price">$450.00</div>
  </div>
  <div class="abs add">Add to Cart</div>
</section>

<section class="abs products">
  <div class="abs tabs"><span class="on">BEST SELLER</span><i>•</i><span>LATEST</span><i>•</i><span>FEATURED</span></div>

  <div class="abs card" style="left:80px">
    <div class="abs photo wood" role="img" aria-label="Photo of a wardrobe with hanging clothes"></div>
    <div class="abs pname">WARDROBE NAME</div><div class="abs stars">★★★★☆</div>
    <div class="abs price">$450</div>
    <svg class="abs heart" width="8" height="7" viewBox="0 0 8 7"><path d="M4 7L.6 3.6A1.9 1.9 0 014 1.2a1.9 1.9 0 013.4 2.4z" fill="#aaa"/></svg>
    <div class="abs add">Add to Cart</div>
  </div>
  <div class="abs card" style="left:211px">
    <div class="abs photo light" role="img" aria-label="Photo of a dining table with four chairs"></div>
    <div class="abs pname">TABLE NAME</div><div class="abs stars">★★★★★</div>
    <div class="abs price">$450</div>
    <svg class="abs heart" width="8" height="7" viewBox="0 0 8 7"><path d="M4 7L.6 3.6A1.9 1.9 0 014 1.2a1.9 1.9 0 013.4 2.4z" fill="#aaa"/></svg>
    <div class="abs add on">Add to Cart</div>
  </div>
  <div class="abs card" style="left:343px">
    <div class="abs photo wood" role="img" aria-label="Photo of a wardrobe with sliding doors open"></div>
    <div class="abs pname">WARDROBE NAME</div><div class="abs stars">★★★★☆</div>
    <div class="abs price">$450</div>
    <svg class="abs heart" width="8" height="7" viewBox="0 0 8 7"><path d="M4 7L.6 3.6A1.9 1.9 0 014 1.2a1.9 1.9 0 013.4 2.4z" fill="#aaa"/></svg>
    <div class="abs add">Add to Cart</div>
  </div>
  <div class="abs card" style="left:474px">
    <div class="abs photo light" role="img" aria-label="Photo of a black dining table with six chairs"></div>
    <div class="abs pname">TABLE NAME</div><div class="abs stars">★★★★★</div>
    <div class="abs price">$450</div>
    <svg class="abs heart" width="8" height="7" viewBox="0 0 8 7"><path d="M4 7L.6 3.6A1.9 1.9 0 014 1.2a1.9 1.9 0 013.4 2.4z" fill="#aaa"/></svg>
    <div class="abs add">Add to Cart</div>
  </div>
</section>

<section class="abs testi" role="img" aria-label="Dimmed photo of a dining room with a dark wood table">
  <h2 class="abs"><b>CUSTOMER</b> TESTIMONIALS</h2>
  <div class="abs quote">
    <div class="abs avatar" role="img" aria-label="Customer portrait"></div>
    <div class="abs mark">“</div>
    <p class="abs">Lorem ipsum dolor sit amet, consectetur adipiscing elit, sed do eiusmod tempor incididunt ut labore et dolore magna aliqua. Ut enim ad minim veniam, quis nostrud exercitation ullamco laboris.</p>
    <div class="abs who"><b>Marta Olsen,</b> Newyork</div>
  </div>
  <div class="abs dots" style="left:331px;top:166px"><span class="on"></span><span></span><span></span><span></span></div>
</section>

<section class="news">
  <svg class="abs news-ico" width="21" height="21" viewBox="0 0 21 21"><rect x="0" y="6" width="21" height="15" fill="#f2b27a"/><path d="M0 6l10.5 8L21 6" fill="#e38f4a"/><rect x="4" y="1" width="13" height="10" fill="#fff" stroke="#e38f4a" stroke-width=".8"/><path d="M0 21l8-7M21 21l-8-7" stroke="#e38f4a" stroke-width=".8"/></svg>
  <h3 class="abs" style="left:106px;top:957px">Subscribe to our Newsletter<br>for latest offers</h3>
  <div class="abs field"><svg width="7" height="5" viewBox="0 0 7 5"><rect width="7" height="5" fill="#f6a6c8"/><path d="M0 0l3.5 2.8L7 0" stroke="#fff" stroke-width=".8" fill="none"/></svg>Enter your email address</div>
  <div class="abs submit">Submit</div>
  <div class="abs vline"></div>
  <div class="abs why">Why Casa Tavola</div>
  <div class="abs feat" style="left:345px;width:50px">
    <svg width="42" height="32" viewBox="0 0 42 32" fill="none" stroke="#f6a6c8" stroke-width="1.2"><rect x="2" y="10" width="22" height="15"/><path d="M24 14h8l6 6v5H24"/><circle cx="10" cy="27" r="3"/><circle cx="32" cy="27" r="3"/><circle cx="16" cy="8" r="6"/><path d="M13 8l2 2 4-4"/></svg>
    FAST DELIVERY
  </div>
  <div class="abs feat" style="left:418px;width:80px">
    <svg width="44" height="32" viewBox="0 0 44 32" fill="none" stroke="#f6a6c8" stroke-width="1.2"><circle cx="26" cy="10" r="8"/><path d="M26 5v10M23 8h5M23 12h5"/><path d="M2 24h10l8 3h14l8-6"/><path d="M12 20h8"/></svg>
    MONEY BACK GUARANTEE
  </div>
  <div class="abs feat" style="left:512px;width:58px">
    <svg width="36" height="32" viewBox="0 0 36 32" fill="none" stroke="#f6a6c8" stroke-width="1.2"><path d="M18 2a14 14 0 11-13 9" stroke-dasharray="3 2"/><path d="M18 2a14 14 0 0113 20"/><text x="11" y="21" font-size="12" font-weight="700" fill="#f6a6c8" stroke="none" font-family="Open Sans,sans-serif">24</text></svg>
    24 HOURS SUPORT
  </div>
</section>

<footer class="abs footer">
  <div class="abs fcol" style="left:78px"><h4>USEFUL LINKS</h4><ul><li>&gt; Home</li><li>&gt; Products</li><li>&gt; Contact Us</li></ul></div>
  <div class="abs fcol" style="left:299px"><h4>MY ACCOUNT</h4><ul><li>&gt; Login</li><li>&gt; Wishlist</li><li>&gt; My Cart</li></ul></div>
  <div class="abs fcol" style="left:494px"><h4>CONTACT US</h4><ul>
    <li class="frow"><svg width="6" height="4.5" viewBox="0 0 7 5"><rect width="7" height="5" fill="#fff"/><path d="M0 0l3.5 2.8L7 0" stroke="#7a3d0b" stroke-width=".8" fill="none"/></svg>hello@casatavola.com</li>
    <li class="frow"><svg width="6" height="6" viewBox="0 0 6 6"><path d="M1 .5l1.3 1.3-.7 1a3.6 3.6 0 001.6 1.6l1-.7L5.5 5 4.8 5.7C2.5 5.5.5 3.5.3 1.2z" fill="#fff"/></svg>000 555 0199</li>
  </ul><div class="fdots"><span></span><span></span><span></span><span></span></div></div>
</footer>

<div class="abs bottom">
  <div class="abs" style="left:79px;top:11px">Copyright 2016 © Casa Tavola - All Rights Reserved</div>
  <div class="abs" style="left:475px;top:11px">Service Level Agreement | Terms of Service</div>
</div>

</body>
</html>
```